Back to School Fair Sponsor Opportunities

We mainly need the cover designed and a continuation of design throughout. The other three pages are basically done just need to be inserted.

Cover will include our Logo, Back to School Fair title at top, photo in center, and date/time at bottom. Please also include "Sponsor Opportunities" or a phrase similar at the bottom.

2 page brochure that's 11x17 full color folded in half (so there are four 8.5x11 panels) with the order form on the back.

Target Market(s)

Corporations

Industry/Entity Type

School

Font styles to use
Serif

Requirements
Must have
• All files must be included with the specifications outlined above.
• Colors that compliment our logo color.
• Please pull detailed information from the files included. (i.e. time/date)
• Order form on the back.
Nice to have
• Please remove the yellow background color to the image if you would like to use a different background.
• Incorporate a few of the event photos into the inside page 2 to break up some of the text.

```html
<!DOCTYPE html>
<html lang="en">
<head>
<meta charset="utf-8">
<title>Back to School Fair – Sponsorship Opportunities</title>
<link href="https://fonts.googleapis.com/css2?family=Tinos:wght@400;700&display=swap" rel="stylesheet">
<style>
  :root {
    --pink: #ef6479;
    --pink-dark: #c94a5e;
    --ink: #1f1f1f;
    --badge: #474747;
    --paper: #ffffff;
    --paper-shade: #f1f1f1;
    --backdrop: #d9d9d9;
  }
  * { margin: 0; padding: 0; box-sizing: border-box; }
  html, body { width: 1200px; height: 850px; overflow: hidden; }
  body {
    background: var(--backdrop);
    font-family: "Tinos", "Times New Roman", serif;
    color: var(--ink);
    position: relative;
  }
  .page {
    position: absolute;
    top: 78px;
    height: 694px;
    background: var(--paper);
  }
  .page--left { left: 65px; width: 535px; background: linear-gradient(90deg, #fff 85%, #e8e8e8 100%); }
  .page--right { left: 600px; width: 535px; background: linear-gradient(90deg, #e4e4e4 0%, #fafafa 10%, #fff 100%); }

  /* left page */
  .title-band {
    position: absolute; left: 47px; top: 2px; width: 443px; height: 75px;
    background: var(--pink); color: #fff; text-align: center; padding-top: 18px;
  }
  .title-band h1 { font-size: 19px; font-weight: 700; line-height: 24px; }
  .title-band p { font-size: 21px; line-height: 26px; }
  .label {
    position: absolute; left: 48px; height: 18px; padding: 0 12px;
    background: var(--pink); color: #fff; font-weight: 700; font-size: 12px;
    line-height: 18px; letter-spacing: .5px;
  }
  .body-text {
    position: absolute; left: 48px; width: 445px; font-size: 8.6px; line-height: 11px;
  }
  .body-text p + p { margin-top: 5px; }
  .inline-fact { position: absolute; left: 134px; font-size: 11px; font-weight: 700; }
  .link { color: var(--pink); }
  .photo {
    position: absolute; top: 510px; width: 135px; height: 80px;
    border: 2px solid var(--pink);
  }
  .photo--1 { left: 48px; background: linear-gradient(135deg, #6f6a73, #c4a789 60%, #7d8aa0); }
  .photo--2 { left: 203px; background: linear-gradient(135deg, #b88c8a, #e7c4b5 50%, #8d7a90); }
  .photo--3 { left: 356px; background: linear-gradient(135deg, #c9d3dc, #d44b4b 55%, #e9e4e2); }
  .range {
    position: absolute; left: 48px; top: 604px; width: 445px;
    font-size: 20.5px; font-weight: 700; text-align: center;
  }
  .footer-band {
    position: absolute; left: 47px; top: 637px; width: 443px; height: 57px;
    background: var(--pink); color: #fff; text-align: center;
    font-weight: 700; font-size: 14px; line-height: 17px; padding-top: 11px;
  }

  /* right page */
  .tier { position: absolute; left: 47px; width: 470px; }
  .tier__head {
    position: relative; width: 313px; height: 33px; background: var(--pink);
    color: #fff; font-weight: 700; font-size: 12.5px; line-height: 33px; text-align: center;
    box-shadow: 0 2px 3px rgba(0,0,0,.15);
  }
  .tier__head::before {
    content: ""; position: absolute; left: 0; top: -6px;
    border-left: 9px solid transparent; border-bottom: 6px solid var(--pink-dark);
    border-right: 0 solid transparent; width: 0;
  }
  .tier__list { list-style: none; margin-top: 5px; }
  .tier__list li {
    position: relative; padding-left: 11px; font-size: 7.4px; line-height: 10.6px;
  }
  .tier__list li::before {
    content: ""; position: absolute; left: 2px; top: 2px; width: 3px; height: 5px;
    border: solid var(--pink); border-width: 0 1.3px 1.3px 0; transform: rotate(40deg);
  }
  .price {
    position: absolute; left: 343px; top: -2px; width: 118px; height: 60px;
    background: var(--badge); color: #fff; text-align: center;
    box-shadow: 0 3px 5px rgba(0,0,0,.3);
  }
  .price::after {
    content: ""; position: absolute; inset: 4px; border: 1px dashed rgba(255,255,255,.7);
  }
  .price strong { display: block; font-size: 19px; line-height: 20px; padding-top: 10px; }
  .price span { display: block; font-size: 11px; font-weight: 700; line-height: 16px; }
</style>
</head>
<body>

<section class="page page--left">
  <header class="title-band">
    <h1>10th Annual Back to School Fair</h1>
    <p>Sponsorship Opportunities &amp; Exhibitor Info</p>
  </header>

  <div class="label" style="top:98px">WHO:</div>
  <div class="body-text" style="top:120px"><p>Meet, interact, and showcase services or products to 7,000+ parents and school-age children.</p></div>

  <div class="label" style="top:146px">WHAT:</div>
  <div class="body-text" style="top:168px"><p>Back to School Fair is an amazing opportunity for businesses to communicate, interact, exhibit products and market services to thousands of Tampa Bay area families on one day under one roof! Attendees want to learn about everything from after-school activity providers, to tutoring services, doctors, yoga and fitness providers, law firms, dentists, food and clothing manufacturers, restaurants, wireless providers, and lots more.</p></div>

  <div class="label" style="top:222px">WHERE:</div>
  <div class="inline-fact" style="top:224px">Lakeside Commons, 410 Lakeside Avenue, Tampa, FL 33609</div>

  <div class="label" style="top:254px">WHEN:</div>
  <div class="inline-fact" style="top:256px">Saturday, August 5, 2017 10 am to 3 pm – SALES TAX HOLIDAY WEEKEND!!</div>

  <div class="label" style="top:287px">WHY:</div>
  <div class="body-text" style="top:309px">
    <p>Bay Family Magazine's Back to School Fair provides the most cost-effective way for you to communicate with 7,000+ local families about your business, product or service.</p>
    <p>Moms and Dads love the "1-Stop Shopping" aspect of Back to School Fair - they can talk to almost 100 activity providers, buy school clothes and supplies (with no sales tax!), get their kids' back to school shopping done, and learn about interesting businesses and products all in one location, face to face. Busy parents appreciate Back to School Fair because they can get all their back to school shopping and planning done in one place on one day!</p>
    <p>Free backpacks to the first 500 kids! Six $500 scholarships raffled off. Additional prizes raffled off throughout the day!</p>
  </div>

  <div class="label" style="top:407px">HOW:</div>
  <div class="body-text" style="top:431px"><p>Go to <span class="link">www.SchoolFairDays.com</span>, <b>CALL - <span class="link">813.555.0142</span></b>, or Email <span class="link">events@bayfamilymag.com</span> to register or for more info!</p></div>

  <div class="label" style="top:458px">COSTS:</div>
  <div class="body-text" style="top:482px"><p>Exhibitor space is $995, with discounts available to Bay Family Magazine advertisers.</p></div>

  <div class="photo photo--1" role="img" aria-label="Event photo: performer entertaining a seated crowd of children"></div>
  <div class="photo photo--2" role="img" aria-label="Event photo: children doing a craft activity at a table"></div>
  <div class="photo photo--3" role="img" aria-label="Event photo: red exhibitor booth inside the shopping plaza"></div>

  <p class="range">Sponsorship levels range from $1,500 to $20,000.</p>

  <footer class="footer-band">Trusted by Local Moms<br>We're Celebrating our 10 Year Anniversary!</footer>
</section>

<section class="page page--right">
  <article class="tier" style="top:12px">
    <h2 class="tier__head">Back to School Fair Naming &amp; "Principal Sponsor"</h2>
    <div class="price"><strong>$20,000</strong><span>Only 1 Available!</span></div>
    <ul class="tier__list">
      <li>Naming rights - Back to School Fair Presented By XYZ Company!</li>
      <li>Branded presence on all event signage and marketing collateral</li>
      <li>Opportunity to display signage throughout Back to School Fair</li>
      <li>Inclusion in all media relations and promotional campaign activates</li>
      <li>Opportunity for spokesperson from Sponsor to participate in radio and television interviews if available</li>
      <li>Largest Exhibitor Space at event – 4-6 tables, 30x30 space!</li>
      <li>Highest Traffic exhibit location at Back to School Fair</li>
      <li>Full Page ad on BACK COVER of Back to School Fair Program</li>
      <li>Full Page ad in THREE ISSUES of Bay Family Magazine</li>
      <li>Leaderboard ad on www.BayFamilyMag.com for THREE MONTHS</li>
      <li>Opportunity to speak or present on Main Stage</li>
    </ul>
  </article>

  <article class="tier" style="top:178px">
    <h2 class="tier__head">Back to School Fair "Favorite Teacher Sponsor"</h2>
    <div class="price"><strong>$7,500</strong><span>Only 1 Available!</span></div>
    <ul class="tier__list">
      <li>Branded presence on some event signage and marketing collateral</li>
      <li>Opportunity to display signage throughout Back to School Fair</li>
      <li>Inclusion in all media relations and promotional campaign activates</li>
      <li>Triple Exhibitor Space – 4 tables, 20x10 space!</li>
      <li>Premium High Traffic exhibit location at Back to School Fair</li>
      <li>Full Page ad on INSIDE FRONT COVER of Back to School Fair Program</li>
      <li>Full Page ad in JULY AND AUGUST ISSUES of Bay Family Magazine</li>
      <li>Leaderboard ad on www.BayFamilyMag.com for two months</li>
      <li>Opportunity to speak or present on Main Stage</li>
    </ul>
  </article>

  <article class="tier" style="top:317px">
    <h2 class="tier__head">Back to School Fair "Straight-A's Sponsor"</h2>
    <div class="price"><strong>$5,000</strong><span>Only 1 Available!</span></div>
    <ul class="tier__list">
      <li>Branded presence on some event signage and marketing collateral</li>
      <li>Opportunity to display signage throughout Back to School Fair</li>
      <li>Double Exhibitor Space – 2 tables, 20x10 space!</li>
      <li>Premium High Traffic exhibit location at Back to School Fair</li>
      <li>Full Page ad in Back to School Fair Program</li>
      <li>Full Page ad in August Issue of Bay Family Magazine and leaderboard on bayfamilymag.com</li>
    </ul>
  </article>

  <article class="tier" style="top:426px">
    <h2 class="tier__head">Back to School Fair "Recess Sponsor"</h2>
    <div class="price"><strong>$2,500</strong><span>Only 4 Available!</span></div>
    <ul class="tier__list">
      <li>Double Exhibitor Space – 2 tables, 20x10 space!</li>
      <li>Premium High Traffic exhibit location at Back to School Fair</li>
      <li>Full Page Ad in Back to School Fair Program</li>
      <li>Half Page Ad in August issue of Bay Family Magazine</li>
      <li>Logo Placement</li>
    </ul>
  </article>

  <article class="tier" style="top:524px">
    <h2 class="tier__head">"Class Sponsor" &amp; Premium Exhibitor</h2>
    <div class="price"><strong>$1,500</strong><span>Only 10 Available!</span></div>
    <ul class="tier__list">
      <li>8x8 Exhibitor Space consisting of 1 table and 2 chairs</li>
      <li>Premium High Traffic exhibit location at Back to School Fair</li>
      <li>Full Page Ad in Back to School Fair Program</li>
      <li>Logo Placement</li>
    </ul>
  </article>

  <article class="tier" style="top:612px">
    <h2 class="tier__head">Exhibitor</h2>
    <div class="price"><strong>$995</strong><span>Only 40 Available!</span></div>
    <ul class="tier__list">
      <li>Stand exhibitor location in Lakeside Commons – upgrade to high traffic space for $500</li>
      <li>8x8 Exhibitor Space consisting of 1 table and 2 chairs</li>
    </ul>
  </article>
</section>

</body>
</html>
```